Non-Profit Web Design - 4 pages + Blog plugin

Brightway Fellowship is a new non-profit 501c3 pending ministry needing a website.

Brightway Fellowship is set up as an "umbrella ministry" which means that it has several "daughter" endeavors under it. So, essentially this website serves as a portal to other sites (some finished, some TBD).

There are 4 core pages:

Home, About, Endeavors, Support + some kind of Blog page/plugin

Design and Coding are required.

Quillet or PageLoom Preferred.

Support page will require a shopping cart for donations.

Please see brief for more information and important
"must haves".

Lanternly (the poster of this job) has closed several successful projects on Pixel Forum in the last 9 months. You will be working for an agency rather then an end user, so the communication is streamlined and less confusing.
Updates

Hey folks, important update here.  First, THANK YOU for all the great designs!

Second, we had approx 12 designers accept this project, only 5 have posted comps.  So, if you're interested, you have 2 days left.  We will be closing the contest promptly on Saturday.

Again, thanks for all the great designs.  We already see at least 2 we can run with.  Well done all!  ~milo

Target Market(s)

This site serves as portal to other edveors (age range 0-99) but the support section of the site will focus on 35-65 & affluent donors

Industry/Entity Type

Communication

Requirements
Must have
• Blog, Ecommerce, Streamlined corporate look without being "harsh".

Must have high quality social sharing (if on PageLoom we prefer Zippy Linkers by Postivore)

Must have Metrica Stats coded in and linked to our account.
Should not have
• NO FLASH!

```html
<!DOCTYPE html>
<html lang="en">
<head>
<meta charset="utf-8">
<title>Brightway Fellowship</title>
<link rel="stylesheet" href="https://fonts.googleapis.com/css2?family=Exo+2:wght@300;400;700;800&display=swap">
<style>
:root{
  --blue:#1565c0;
  --blue-dark:#0b4a9c;
  --ink:#2b2b2b;
  --text:#444;
  --muted:#8a8a8a;
  --dark:#262626;
  --paper:#e4e1dc;
  --paper-2:#d9d6d1;
  --white:#fff;
  --icon:#5a3a2a;
}
*{box-sizing:border-box;margin:0;padding:0}
html,body{width:1200px;height:893px;overflow:hidden}
body{position:relative;font-family:"Exo 2",sans-serif;background:var(--paper);color:var(--text)}
a{color:inherit;text-decoration:none}
.topline{position:absolute;left:0;top:0;width:1200px;height:5px;background:var(--blue)}
.site-header{position:absolute;left:0;top:5px;width:1200px;height:89px;background:var(--white)}
.brand{position:absolute;left:172px;top:18px;display:flex;align-items:center;gap:8px}
.brand-mark{width:18px;height:18px;border-radius:50%;background:var(--blue)}
.brand-name{font-weight:700;font-size:19px;color:var(--blue);letter-spacing:.5px;text-transform:uppercase}
.brand-tag{position:absolute;left:198px;top:43px;font-size:7px;color:var(--muted);text-transform:uppercase;letter-spacing:.4px;width:200px}
.utility{position:absolute;right:171px;top:14px;display:flex;align-items:center;font-size:12px;font-weight:300;color:var(--ink);gap:5px}
.utility .cart{width:18px;height:12px;margin-left:4px}
.social-dots{display:flex;gap:6px;margin-left:9px}
.social-dots span{width:25px;height:25px;border-radius:50%;background:var(--icon)}
.main-nav{position:absolute;right:171px;top:53px;display:flex;align-items:center;font-size:16px;color:var(--ink)}
.main-nav a{padding:0 13px;border-left:1px solid #bbb;line-height:14px}
.main-nav a:last-child{padding-right:0}
.main-nav a.active{background:var(--blue);color:var(--white);border:0;border-radius:14px;line-height:27px;padding:0 16px;margin-right:12px}
.main-nav a.active+a{border-left:1px solid #bbb}
.hero{position:absolute;left:0;top:94px;width:1200px;height:417px;background:linear-gradient(90deg,#dcd9d3 0%,#d9d6cf 45%,#c8c4b4 60%,#b5ab86 75%,#d0cbbd 90%,#dedbd5 100%)}
.hero-photo{position:absolute;left:540px;top:0;width:540px;height:417px;background:radial-gradient(ellipse at 55% 55%,#a08462 0%,#b9a27b 35%,rgba(200,190,160,.4) 65%,rgba(220,217,211,0) 85%)}
.hero-copy{position:absolute;left:172px;top:84px;width:380px}
.hero-title{font-weight:800;font-size:39px;line-height:43px;letter-spacing:-2.2px;color:var(--ink);text-transform:uppercase}
.hero-text{margin-top:9px;font-size:9.6px;line-height:13px;color:var(--ink);text-transform:uppercase}
.hero-actions{position:absolute;left:171px;top:399px;display:flex;gap:10px}
.btn{display:block;width:120px;height:34px;border-radius:17px;background:linear-gradient(#2b7fd8,var(--blue-dark));color:var(--white);font-size:17px;text-align:center;line-height:34px;box-shadow:0 2px 3px rgba(0,0,0,.25)}
.slider-dots{position:absolute;left:171px;top:485px;display:flex;gap:6px}
.slider-dots span{width:14px;height:14px;border-radius:50%;background:var(--white)}
.slider-dots span.on{background:var(--ink)}
.band{position:absolute;left:0;top:511px;width:1200px;height:6px;background:var(--blue)}
.features{position:absolute;left:0;top:517px;width:1200px;height:183px;background:var(--dark)}
.feature{position:absolute;top:21px;width:240px}
.feature-head{display:flex;align-items:center;gap:9px;height:66px}
.feature-head svg{flex:none}
.feature-title{font-weight:700;font-size:32px;line-height:30px;letter-spacing:-2px;color:var(--white);text-transform:uppercase}
.feature-text{margin-top:16px;font-size:9.6px;line-height:13px;color:#bbb;text-transform:uppercase;width:230px}
.feature-more{display:block;margin-top:7px;font-size:11px;font-weight:700;color:var(--blue);text-transform:uppercase;letter-spacing:-.3px}
.lower h2{font-weight:800;font-size:17px;letter-spacing:-.8px;color:var(--ink);text-transform:uppercase;border-bottom:1px dotted #aaa;padding-bottom:1px}
.col{position:absolute;top:730px}
.signup p{font-size:13px;line-height:13px;font-weight:300;color:var(--text);margin-top:2px}
.signup-form{display:flex;margin-top:14px}
.signup-form .field{width:174px;height:25px;background:linear-gradient(#e8e8e8,#fff);border:1px solid #ccc;border-radius:3px 0 0 3px}
.signup-form .send{width:53px;height:25px;background:var(--blue);color:var(--white);font-size:13px;line-height:25px;text-align:center;border-radius:0 12px 12px 0}
.events li{list-style:none;font-size:13px;font-weight:300;line-height:25px;border-bottom:1px dotted #aaa;color:var(--text)}
.contact address{font-style:normal;font-size:13.5px;font-weight:300;line-height:15px;margin-top:6px;color:var(--text)}
.share-row{display:flex;gap:5px;margin-top:8px}
.share-row span{width:25px;height:25px;border-radius:4px;background:linear-gradient(#6fa9d9,#2c6fae)}
.share-row span:nth-child(1){background:linear-gradient(#e35b4b,#b3281b)}
.share-row span:nth-child(2){background:linear-gradient(#eee,#bbb)}
.share-row span:nth-child(7){background:linear-gradient(#f79a4a,#d9621a)}
.site-footer{position:absolute;left:0;top:850px;width:1200px;height:43px;background:var(--paper-2);font-size:10.5px;color:var(--muted);text-transform:uppercase}
.footer-links{position:absolute;left:173px;top:16px}
.copyright{position:absolute;right:171px;top:16px}
</style>
</head>
<body>
<div class="topline"></div>
<header class="site-header">
  <a class="brand" href="#"><span class="brand-mark"></span><span class="brand-name">Brightway Fellowship</span></a>
  <div class="brand-tag">Using every avenue to proclaim Christ and biblical truth</div>
  <div class="utility">
    <a href="#">My Account</a> /
    <svg class="cart" viewBox="0 0 18 12"><path d="M0 1h3l2 7h10l2-6H4" fill="none" stroke="#333" stroke-width="1.5"/><circle cx="6" cy="10.5" r="1.3" fill="#333"/><circle cx="14" cy="10.5" r="1.3" fill="#333"/></svg>
    <a href="#">My Cart</a> / <a href="#">Go To Checkout</a>
    <div class="social-dots"><span></span><span></span><span></span></div>
  </div>
  <nav class="main-nav">
    <a class="active" href="#">HOME</a><a href="#">ABOUT</a><a href="#">ENDEAVORS</a><a href="#">SUPPORT</a><a href="#">BLOG</a><a href="#">CONTACT</a>
  </nav>
</header>

<section class="hero">
  <div class="hero-photo" role="img" aria-label="Photo of a smiling bearded man in a jacket holding a Bible, outdoors"></div>
  <div class="hero-copy">
    <h1 class="hero-title">“Use every avenue to proclaim Christ and biblical truth”.</h1>
    <p class="hero-text">Lorem ipsum dolor sit amet, consectetuer adipiscing elit, sed diam nonummy nibh euismod tincidunt ut laoreet dolore magna aliquam erat volutpat. Ut wisi enim ad minim veniam, quis nostrud exerci tation ullamcorper suscipit lobortis nisl ut aliquip ex ea commodo consequat.</p>
  </div>
</section>
<div class="hero-actions"><a class="btn" href="#">DONATE</a><a class="btn" href="#">VOLUNTEER</a></div>
<div class="slider-dots"><span class="on"></span><span></span><span></span></div>
<div class="band"></div>

<section class="features">
  <article class="feature" style="left:171px">
    <div class="feature-head">
      <svg width="66" height="66" viewBox="0 0 66 66"><rect x="3" y="8" width="60" height="55" rx="5" fill="none" stroke="#aaa" stroke-width="5"/><rect x="3" y="8" width="60" height="12" fill="#aaa"/><rect x="14" y="2" width="6" height="12" rx="2" fill="#aaa"/><rect x="46" y="2" width="6" height="12" rx="2" fill="#aaa"/><text x="33" y="56" text-anchor="middle" font-family="Exo 2,sans-serif" font-weight="800" font-size="32" fill="#aaa">7</text></svg>
      <h3 class="feature-title">Events &amp;<br>Management</h3>
    </div>
    <p class="feature-text">Lorem ipsum dolor sit amet, consectetuer adipiscing elit, sed diam nonummy nibh euismod tincidunt ut laoreet dolore.</p>
    <a class="feature-more" href="#">Raead more</a>
  </article>
  <article class="feature" style="left:490px">
    <div class="feature-head">
      <svg width="66" height="66" viewBox="0 0 66 66"><path d="M2 10l18 8 26-8 18 8v46l-18-8-26 8-18-8z" fill="#aaa"/><circle cx="33" cy="20" r="12" fill="#262626"/><path d="M33 10a9 9 0 0 1 9 9c0 7-9 17-9 17s-9-10-9-17a9 9 0 0 1 9-9z" fill="#aaa"/><circle cx="33" cy="19" r="3.5" fill="#262626"/></svg>
      <h3 class="feature-title">Times &amp;<br>Location</h3>
    </div>
    <p class="feature-text">Lorem ipsum dolor sit amet, consectetuer adipiscing elit, sed diam nonummy nibh euismod tincidunt ut laoreet dolore.</p>
    <a class="feature-more" href="#">Raead more</a>
  </article>
  <article class="feature" style="left:782px;width:260px">
    <div class="feature-head">
      <svg width="66" height="66" viewBox="0 0 66 66"><path d="M20 26v-8a13 13 0 0 1 26 0v8" fill="none" stroke="#aaa" stroke-width="6"/><rect x="2" y="24" width="62" height="40" rx="9" fill="#aaa"/><circle cx="33" cy="42" r="5" fill="#262626"/></svg>
      <h3 class="feature-title">Ministries &amp;<br>Rules</h3>
    </div>
    <p class="feature-text">Lorem ipsum dolor sit amet, consectetuer adipiscing elit, sed diam nonummy nibh euismod tincidunt ut laoreet dolore.</p>
    <a class="feature-more" href="#">Raead more</a>
  </article>
</section>

<section class="lower">
  <div class="col signup" style="left:173px;width:222px">
    <h2>Get connected.</h2>
    <p>Sign up to receive the Brightway Fellowship Newsletter!</p>
    <div class="signup-form"><span class="field"></span><span class="send">SEND</span></div>
  </div>
  <div class="col events" style="left:503px;width:222px">
    <h2>Current events.</h2>
    <ul>
      <li>Recent LHA news &amp; announcements</li>
      <li>Lorem ipsum dolor sit amet</li>
      <li>ullamcorper suscipit lobortis nisl ut.</li>
    </ul>
  </div>
  <div class="col contact" style="left:776px;width:260px">
    <h2 style="width:222px">Contact us.</h2>
    <address>LHA (Linden Hill Association)<br>214 Linden Street, Dayton, OH 45402<br>(555) 014-2290, email us, or find out more.</address>
    <div class="share-row"><span></span><span></span><span></span><span></span><span></span><span></span><span></span><span></span></div>
  </div>
</section>

<footer class="site-footer">
  <div class="footer-links">About us | Our programs | Donate | Volunteer | Leaders &amp; Staff | Employee login | Sitemap</div>
  <div class="copyright">©2008 LHA. All rights reserved.</div>
</footer>
</body>
</html>
```